Illustrate a statistic and its significance

Please create a graphical representation of the success rate of the Lanton Procedure for our website. The Lanton Procedure has a success rate of 80%. This means the procedure is successful for 8 out of every 10 people. An 80% success rate by itself is great. However, it's even more impressive when you consider that the only people we perform this procedure on are patients who have exhausted conventional treatment options for migraines and headaches. I would really like to emphasize both the success rate and the type of patients we are successful in treating with this procedure.
For example, you could create an illustration of outlines of 10 people with 8 of them shaded in, which would represent an 80% success rate. Then, underneath this image, you could add a bullet list of the types of treatments patients (such as the 10 figures in the image) have tried before coming to us/having this procedure, which include the following:
Prescription medications
Trigger point injections
Nerve blocks
Migraine surgery
Velquin
Chiropractic care
Physical therapy
Biofeedback
Massage
Acupuncture
Or maybe there is another/better way to represent this statistic graphically? I'm just looking for an effective illustration of this important statistic and its significance.
Our brand colors are red (#fd444a) and blue (#214170)
Thank you!
Target Market(s)
People who suffer from chronic migraines and headaches
Industry/Entity Type
Healthcare/Medical
Other font styles liked:
- Athiti

```html
<!DOCTYPE html>
<html lang="en">
<head>
<meta charset="utf-8">
<title>Lanton Procedure – Success Rate</title>
<link rel="stylesheet" href="https://fonts.googleapis.com/css2?family=Athiti:wght@400;500;600;700&family=Exo+2:wght@700;800&display=swap">
<style>
  :root {
    --red: #e9474f;
    --blue: #1f3f70;
    --ink: #1c1c1c;
    --bg: #eeeeee;
    --photo-light: #d9d9d9;
    --photo-dark: #5a5a5a;
  }
  * { box-sizing: border-box; margin: 0; padding: 0; }
  html, body { width: 1200px; height: 652px; overflow: hidden; background: var(--bg); }
  .canvas {
    position: relative; width: 1200px; height: 652px; overflow: hidden;
    background: var(--bg); font-family: "Athiti", sans-serif;
  }
  .kicker {
    position: absolute; left: 74px; top: 55px; width: 393px; height: 30px;
    background: var(--blue); color: #fff; font-size: 18px; font-weight: 500;
    line-height: 30px; padding-left: 9px; letter-spacing: 0.4px;
  }
  .headline {
    position: absolute; left: 72px; top: 88px; color: var(--red);
    font-family: "Exo 2", sans-serif; font-weight: 800; font-size: 71px;
    line-height: 76px; letter-spacing: 1px;
  }
  .figures { position: absolute; left: 78px; top: 259px; }
  .tagline {
    position: absolute; left: 77px; top: 376px; color: var(--blue);
    font-size: 29px; font-weight: 500; letter-spacing: 1px; white-space: nowrap;
    display: flex; align-items: center;
  }
  .rate {
    display: inline-flex; align-items: center; justify-content: center;
    width: 66px; height: 66px; border-radius: 50%; background: var(--red);
    color: #fff; font-weight: 700; font-size: 27px; margin: 0 10px 0 8px;
  }
  .services-title {
    position: absolute; left: 75px; top: 446px; color: var(--red);
    font-size: 27px; font-weight: 600; letter-spacing: 0.8px;
  }
  .services-rule {
    position: absolute; left: 78px; top: 484px; width: 168px; height: 1.5px; background: var(--blue);
  }
  .services {
    position: absolute; top: 502px; list-style: none; color: var(--ink);
    font-size: 19px; line-height: 23.4px; letter-spacing: 0.6px;
  }
  .services li::before { content: "•"; margin-right: 6px; }
  .services.col-a { left: 78px; }
  .services.col-b { left: 313px; }
  .photo {
    position: absolute; left: 700px; top: 0; width: 500px; height: 652px;
    background:
      radial-gradient(ellipse 45% 60% at 65% 75%, var(--photo-dark) 0%, rgba(90,90,90,0.6) 45%, rgba(238,238,238,0) 75%),
      radial-gradient(circle at 52% 14%, rgba(233,71,79,0.22) 0%, rgba(238,238,238,0) 18%),
      linear-gradient(90deg, var(--bg) 0%, var(--photo-light) 50%, var(--bg) 100%);
  }
</style>
</head>
<body>
<main class="canvas">
  <div class="kicker">Exhausted with conventional treatment for</div>
  <h1 class="headline">Migraines<br>and Headaches?</h1>

  <svg class="figures" width="560" height="98" viewBox="0 0 560 98" aria-label="8 out of 10 people filled in">
    <defs>
      <g id="person">
        <circle cx="22" cy="10" r="10"/>
        <path d="M6 24 H38 a6 6 0 0 1 6 6 V58 h-5 V40 h-3 V97 h-7 V64 h-2 V97 h-7 V40 h-3 V58 H0 V30 a6 6 0 0 1 6 -6 Z"/>
      </g>
    </defs>
    <g fill="#1f3f70">
      <use href="#person" x="0"/><use href="#person" x="57"/><use href="#person" x="114"/><use href="#person" x="171"/>
      <use href="#person" x="228"/><use href="#person" x="286"/><use href="#person" x="343"/><use href="#person" x="400"/>
    </g>
    <g fill="none" stroke="#1f3f70" stroke-width="1">
      <use href="#person" x="457"/><use href="#person" x="514"/>
    </g>
  </svg>

  <p class="tagline">We offer a procedure of <span class="rate">80%</span> success rate</p>

  <h2 class="services-title">Our Services</h2>
  <div class="services-rule"></div>
  <ul class="services col-a">
    <li>Prescription medications</li>
    <li>Trigger point injections</li>
    <li>Nerve blocks</li>
    <li>Migraine surgery</li>
    <li>Velquin</li>
  </ul>
  <ul class="services col-b">
    <li>Chiropractic care</li>
    <li>Physical therapy</li>
    <li>Biofeedback</li>
    <li>Massage</li>
    <li>Acupuncture</li>
  </ul>

  <div class="photo" role="img" aria-label="Black and white photo of a woman holding her temple in pain, with a red glow at her forehead"></div>
</main>
</body>
</html>
```